CTWI application splash screen

We need a 1024x768 image for use as an application splash screen.
The image will be displayed full screen on an 10 inch industrial PC 1024x768 screen while our application is launching. The image should convey that the application is "Waiting for connection to Wi-Fi access point..." and include a graphic of the industrial PC connected to the access point via an Ethernet cable. A list of troubleshooting steps should be included at the bottom of the image. The troubleshooting steps should not be the main focus of the image and should be shown in a smaller font (but still readable at 1024x768 displayed on a 10 inch screen).
I will include a mock up of the general idea of what we are looking for as well as image files for the industrial PC, a screenshot of our application to show on the PC's screen and the AP.
For general look and feel and a sense of corporate branding please review our website https://corvanetillageworks.com/. The splash screen should reflect corporate branding.
Target Market(s)
Users of our application
Industry/Entity Type
Agriculture

```html
<!DOCTYPE html>
<html lang="en">
<head>
<meta charset="utf-8">
<title>CTWI – Waiting for connection</title>
<link rel="stylesheet" href="https://fonts.googleapis.com/css2?family=Poppins:wght@400;500;600;700&display=swap">
<style>
  :root {
    --brand-green: #2bb673;
    --ink: #1f1f1f;
    --band-dark: #222222;
    --paper: #ffffff;
    --device-frame: #3a3d42;
    --device-screen: #dfe6e1;
    --ap-body: #eef0f2;
    --ap-shade: #c9cdd1;
  }
  * { box-sizing: border-box; margin: 0; padding: 0; }
  html, body { width: 1200px; height: 900px; overflow: hidden; background: var(--paper); }
  body { font-family: "Poppins", sans-serif; color: var(--ink); }

  .splash { position: relative; width: 1200px; height: 900px; overflow: hidden; background: var(--paper); }

  .brand { position: absolute; left: 44px; top: 34px; }
  .brand-row { display: flex; align-items: center; gap: 12px; }
  .brand-mark { width: 40px; height: 40px; background: var(--brand-green); }
  .brand-name { font-size: 52px; font-weight: 700; line-height: 1; color: var(--ink); letter-spacing: 2px; }
  .brand-tagline { margin-top: 10px; font-size: 21px; font-weight: 400; color: var(--brand-green); border-bottom: 1px solid var(--ink); padding-bottom: 2px; }

  .headline { position: absolute; left: 330px; width: 700px; top: 70px; text-align: center; font-weight: 700; font-size: 64px; line-height: 81px; color: var(--ink); }
  .headline .accent { color: var(--brand-green); }

  .diagram { position: absolute; left: 0; top: 0; width: 1200px; height: 640px; }

  .device-screen { position: absolute; left: 56px; top: 326px; width: 272px; height: 216px; border-radius: 14px; background: var(--device-frame); }
  .device-screen-inner { position: absolute; left: 18px; top: 18px; right: 18px; bottom: 34px; border-radius: 4px; background: linear-gradient(180deg, var(--device-screen), #bfe3cd); }
  .access-point { position: absolute; left: 1040px; top: 228px; width: 64px; height: 230px; border-radius: 10px; background: linear-gradient(90deg, var(--ap-body), var(--ap-shade)); }

  .label { position: absolute; font-size: 22px; font-weight: 500; color: var(--ink); white-space: nowrap; transform: translateX(-50%); }
  .label-computer { left: 191px; top: 552px; }
  .label-cable { left: 680px; top: 462px; }
  .label-ap { left: 1066px; top: 520px; }

  .footer-shapes { position: absolute; left: 0; top: 0; width: 1200px; height: 900px; }

  .troubleshooting { position: absolute; left: 470px; top: 662px; width: 700px; color: var(--paper); }
  .troubleshooting h2 { margin-left: 61px; font-size: 20px; font-weight: 700; margin-bottom: 18px; }
  .steps { list-style: none; font-size: 14.6px; line-height: 21px; }
  .steps > li { position: relative; padding-left: 14px; }
  .steps > li::before { content: "•"; position: absolute; left: 0; }
  .sub-steps { list-style: none; padding-left: 42px; }
  .sub-steps li { position: relative; padding-left: 14px; }
  .sub-steps li::before { content: "◦"; position: absolute; left: 0; }
</style>
</head>
<body>
<main class="splash">

  <svg class="footer-shapes" viewBox="0 0 1200 900" aria-hidden="true">
    <polygon points="0,642 676,600 1200,628 1200,900 0,900" fill="var(--band-dark)"/>
    <polygon points="383,636 1200,632 1200,900 375,900 428,752" fill="var(--brand-green)"/>
  </svg>

  <header class="brand">
    <div class="brand-row">
      <span class="brand-mark"></span>
      <span class="brand-name">CTWI</span>
    </div>
    <p class="brand-tagline">Corvane Tillage Works Inc.</p>
  </header>

  <h1 class="headline">Waiting for<br>connection to<br><span class="accent">Wi-Fi access point...</span></h1>

  <svg class="diagram" viewBox="0 0 1200 640" aria-hidden="true">
    <polyline points="348,506 1070,506 1070,478" fill="none" stroke="var(--ink)" stroke-width="3"/>
    <rect x="336" y="499" width="16" height="14" rx="2" fill="var(--ink)"/>
    <rect x="1063" y="466" width="14" height="16" rx="2" fill="var(--ink)"/>
  </svg>

  <div class="device-screen" role="img" aria-label="Industrial tractor cab computer showing the seeding application screen">
    <div class="device-screen-inner"></div>
  </div>
  <div class="access-point" role="img" aria-label="Outdoor Wi-Fi access point with two antennas"></div>

  <span class="label label-cable">Ethernet cable</span>
  <span class="label label-computer">Tractor cab computer</span>
  <span class="label label-ap">Wi-Fi Access Point</span>

  <section class="troubleshooting">
    <h2>Troubleshooting steps:</h2>
    <ul class="steps">
      <li>This screen should only be visible for a short time on boot.</li>
      <li>If this screen stays visible for more than a minute:
        <ul class="sub-steps">
          <li>Verify that when the cab computer is powered up the Wi-Fi Access Point<br>(AP) is also powered up (indicated by green light on side of the AP).</li>
          <li>Check the Ethernet cable for damage and replace if damaged.</li>
          <li>Contact CTWI support for further assistance.</li>
        </ul>
      </li>
    </ul>
  </section>

</main>
</body>
</html>
```